Brightfold Partners Website

Brightfold Partners Advisory Services is a company which provides specialised advise in carbon markets, climate policy, landscapes, resilience and change. We are based in Australia but the majority of our business is global. Our clients range from governments to large corporates and not for profit organisations.
Our focus is on developing the capabilities of government officials, business decision makers and land managers so they can better navigate the complexity of climate change and sustainability.
We are looking for a website that is consistent with the high end professional services which we provide to serious players.
I have attached two versions of our logo. I have also attached the back of our business card so you can get a sense of what we hand to potential clients.

Target Market(s)

Professional individuals, decision makers, board members etc, government officials.

Industry/Entity Type

Government

Number of Pages Required

4 page

Font styles to use
Serif
Sans Serif

Requirements
Must have
• Please provide
• 1. Home page
• 2. Service page template
• 3. Contact page
• 4. Lead expert profile page

```html
<!DOCTYPE html>
<html lang="en">
<head>
<meta charset="utf-8">
<title>Brightfold Partners Advisory Services</title>
<link rel="stylesheet" href="https://fonts.googleapis.com/css2?family=Source+Serif+4:wght@400&family=Lato:wght@300&family=Open+Sans:wght@400&display=swap">
<style>
  :root {
    --nav-bg: #031114;
    --button-bg: #1d5662;
    --hero-top: #1f5a63;
    --hero-mid: #13434b;
    --hero-low: #0f3a41;
    --white: #ffffff;
    --heading-teal: #1d4a55;
    --body-grey: #4a4a4a;
    --rule-grey: #e4e4e4;
    --band-grey: #f8f8f8;
  }
  * { margin: 0; padding: 0; box-sizing: border-box; }
  html, body { width: 1200px; height: 900px; overflow: hidden; background: var(--white); }
  body { position: relative; font-family: "Lato", sans-serif; }

  .site-header {
    position: absolute; left: 0; top: 0; width: 1200px; height: 81px;
    background: var(--nav-bg);
  }
  .brand {
    position: absolute; left: 265px; top: 21px;
    display: flex; align-items: center; gap: 8px;
  }
  .brand-mark {
    width: 34px; height: 34px; border-radius: 50%;
    border: 1.5px solid #cfd6d8;
  }
  .brand-name {
    font-family: "Source Serif 4", serif; font-weight: 400;
    color: var(--white); font-size: 19px; line-height: 19px;
    letter-spacing: 1.5px; text-transform: uppercase;
  }
  .main-nav {
    position: absolute; left: 473px; top: 30px;
    display: flex; gap: 24px;
    font-family: "Open Sans", sans-serif; font-size: 16px; color: var(--white);
  }
  .contact-cta {
    position: absolute; left: 797px; top: 18px; width: 141px; text-align: center;
    font-family: "Open Sans", sans-serif;
  }
  .email-button {
    display: block; margin: 0 auto; width: 124px; height: 31px; line-height: 31px;
    background: var(--button-bg); color: var(--white); font-size: 15px; border-radius: 2px;
  }
  .call-line { margin-top: 2px; font-size: 12.5px; color: #e6ecee; }

  .hero {
    position: absolute; left: 0; top: 81px; width: 1200px; height: 463px;
    background: linear-gradient(160deg, var(--hero-top) 0%, var(--hero-mid) 45%, var(--hero-low) 100%);
  }
  .hero-title {
    position: absolute; left: 0; top: 115px; width: 1200px; text-align: center;
    font-family: "Source Serif 4", serif; font-weight: 400;
    font-size: 49px; color: var(--white); line-height: 70px;
  }
  .hero-intro {
    position: absolute; left: 0; top: 188px; width: 1200px; text-align: center;
    font-size: 19px; line-height: 35.5px; color: #eef3f4; font-weight: 300;
  }

  .what-we-do { position: absolute; left: 0; top: 544px; width: 1200px; height: 340px; }
  .section-title {
    position: absolute; left: 0; top: 63px; width: 1200px; text-align: center;
    font-family: "Source Serif 4", serif; font-weight: 400;
    font-size: 24px; color: var(--heading-teal);
  }
  .section-rule {
    position: absolute; left: 462px; top: 116px; width: 276px; height: 1px;
    background: var(--rule-grey);
  }
  .section-text {
    position: absolute; left: 0; top: 148px; width: 1200px; text-align: center;
    font-size: 19px; line-height: 35.5px; color: var(--body-grey); font-weight: 300;
  }
  .next-band {
    position: absolute; left: 0; top: 884px; width: 1200px; height: 16px;
    background: var(--band-grey);
  }
</style>
</head>
<body>
  <header class="site-header">
    <div class="brand">
      <span class="brand-mark"></span>
      <span class="brand-name">Brightfold<br>Partners</span>
    </div>
    <nav class="main-nav">
      <span>Home</span>
      <span>Services</span>
      <span>Lead Expert Profile</span>
    </nav>
    <div class="contact-cta">
      <span class="email-button">Email Us</span>
      <p class="call-line">or call +44 7700 900 418</p>
    </div>
  </header>

  <section class="hero" role="img" aria-label="Rugged coastal cliffs meeting the sea, under a deep teal tint">
    <h1 class="hero-title">Leading environmental advisors.</h1>
    <p class="hero-intro">
      Brightfold Partners provides expert advisory services in carbon markets,<br>
      climate policy, landscapes and change. Our focus is on developing the capabilities<br>
      of government officials, business decision makers and land managers so they can better<br>
      navigate the complexity of climate change &amp; sustainability.
    </p>
  </section>

  <section class="what-we-do">
    <h2 class="section-title">What We Do</h2>
    <div class="section-rule"></div>
    <p class="section-text">
      We provide environmental advisory services across a number of specialised areas.<br>
      All of our advisory services are tailored to the situation and needs of the client,<br>
      so no two engagements are the same.
    </p>
  </section>

  <div class="next-band"></div>
</body>
</html>
```